The Bright Meadow Web site design

The Bright Meadow is a new wellness concept (website) in Singapore offering a 360-degree source for health and wellbeing.

Please see the following two websites as examples to reference for layout

http://brovalkits.com/preview/Vantor/

www.zt-nimbo.farpeakhosts.com/

Please see below websites for examples of look feel and design. Something clean and similar is required for the BM.

www.sunnorafolkla.com

http://www.tallowpinehub.com/

Specs:

• A combination of the Vantor and ZT Nimbo sites

• Ad banners – must be able to have ad banner at top of page (under BM branding) and also banners on right hand side, plus at the bottom of page.

• Must have a search facility

• ‘Subscribe to newsletters’ built in and back end to hold subscribers

• Top main part to hold main features and newest stories scrolling

• Must be mobile friendly (Vantor is, zt-nimbo isn’t)

• Top of the page branding smaller than vantor so it doesn’t take up so much eyeball equity. Zt-nimbo is better at this.

• Must be image rich and be able to house videos

• Social media links in first half of the page to pixagrove, kinlobby and murlotalk.

• Tabs – about us, move, glow, escape, be, contact us

• Must be an easy CMS backend for easy uploading.

• Colours – white, green, blue, grey – very clean and clear, projecting bright meadow healthy lifestyle.

• Space for advertising

Easy backend for ease of upload such as wordpress

```html
<!DOCTYPE html>
<html lang="en">
<head>
<meta charset="utf-8">
<title>The Bright Meadow</title>
<link href="https://fonts.googleapis.com/css2?family=Open+Sans:wght@300;400;600&family=Josefin+Sans:wght@300;400&display=swap" rel="stylesheet">
<style>
:root{
  --green:#2aa85a;
  --green-dark:#1f8f4a;
  --blue:#3a8fe0;
  --blue-deep:#2f7fd4;
  --sky:#4ab3e6;
  --red:#e0342c;
  --ink:#2b2b2b;
  --grey:#6d6d6d;
  --muted:#9a9a9a;
  --line:#e4e4e4;
  --soft:#f4f4f4;
  --star:#f0b400;
}
*{margin:0;padding:0;box-sizing:border-box}
html,body{width:720px;height:1200px;overflow:hidden;background:#fff}
body{position:relative;font-family:'Open Sans',sans-serif;color:var(--ink)}
.abs{position:absolute}
.topbar{left:0;top:0;width:720px;height:22px;border-bottom:1px solid var(--line);font-size:8px;color:var(--muted)}
.topbar .welcome{left:61px;top:6px}
.topbar .social{right:58px;top:6px;font-size:7px;color:var(--muted);letter-spacing:.2px}
.logo{left:58px;top:36px;font-family:'Josefin Sans',sans-serif;font-weight:300;font-size:22px;color:var(--green)}
.ad-top{left:422px;top:31px;width:240px;height:35px;border:1px solid var(--line);background:#fafafa;color:#b8b8b8;font-size:11px;display:flex;align-items:center;justify-content:center;font-weight:300}
.nav{left:61px;top:77px;width:600px;height:21px;border-top:1px solid var(--line);border-bottom:1px solid var(--line);display:flex;font-size:8px;color:var(--muted);letter-spacing:.3px}
.nav a{display:flex;align-items:center;padding:0 17px;color:inherit;text-decoration:none}
.nav a.active{background:var(--green);color:#fff;width:75px;justify-content:center;padding:0;font-weight:600}
.search{left:518px;top:80px;width:139px;height:15px;background:var(--soft);border:1px solid var(--line);font-size:6px;color:#b5b5b5;padding:3px 6px}
.search-btn{left:641px;top:80px;width:16px;height:15px;background:var(--green)}
.hero{left:61px;top:110px;width:600px;height:256px;background:linear-gradient(90deg,#fdfdfd 0%,#f6f4f2 45%,#ede9e5 70%,#e7ece9 100%);border:1px solid var(--line);overflow:hidden}
.hero-photo{position:absolute;right:0;top:0;width:290px;height:256px;background:linear-gradient(180deg,#ece7e0 0%,#e4ddd5 55%,#cfe3cf 78%,#7eb6d6 100%)}
.hero h1{position:absolute;left:41px;top:56px;font-weight:400;font-size:22px;line-height:25px;color:#222}
.hero h2{position:absolute;left:41px;top:116px;font-weight:400;font-size:13px;color:var(--sky)}
.hero p{position:absolute;left:41px;top:142px;width:280px;font-size:6.4px;line-height:10px;color:var(--grey)}
.hero .btn{position:absolute;left:41px;top:178px;width:121px;height:26px;background:linear-gradient(180deg,#38c36c,var(--green-dark));color:#114d28;font-size:6.5px;font-weight:600;display:flex;align-items:center;padding-left:40px}
.hero .btn svg{position:absolute;left:10px;top:7px}
.arrow{position:absolute;top:129px;width:14px;height:14px;background:rgba(255,255,255,.6);border:1px solid #ddd}
.features{left:61px;top:394px;width:600px}
.feature{position:absolute;width:130px;text-align:center}
.feature .icon{width:38px;height:38px;border-radius:50%;margin:0 auto;display:flex;align-items:center;justify-content:center}
.feature h3{font-weight:400;font-size:10px;margin-top:10px;color:#222}
.feature p{font-size:6.6px;line-height:10px;margin-top:7px;color:#333}
.sec-title{font-size:11px;color:#222;display:flex;align-items:center;gap:6px}
.sec-title .ring{width:15px;height:15px;border:1.4px solid #333;border-radius:50%;display:flex;align-items:center;justify-content:center}
.pager{display:flex;gap:6px}
.pager span{width:12px;height:12px;border:1px solid #ccc;border-radius:50%;font-size:7px;color:#999;display:flex;align-items:center;justify-content:center}
.story-lead{left:61px;top:559px;width:199px;height:199px;border:1px solid var(--line);border-bottom:3px solid var(--green)}
.story-lead .ph{height:91px;background:linear-gradient(135deg,#e9e4dc,#cdd7e2 55%,#4a8fd0)}
.story-lead h4{font-weight:400;font-size:8px;margin:6px 7px 0}
.meta{font-size:5.5px;color:var(--muted);margin:5px 7px 0}
.meta b{font-weight:400;color:var(--red)}
.stars{font-size:7px;color:#ccc;margin:2px 7px 0;letter-spacing:-.5px}
.stars i{font-style:normal;color:var(--star)}
.story-lead p{font-size:6px;line-height:9.5px;color:var(--grey);margin:7px 7px 0}
.story-lead p em{color:var(--red)}
.card{position:absolute;width:104px;height:97px;border:1px solid var(--line)}
.card .ph{height:47px}
.card h4{font-weight:400;font-size:7px;line-height:11px;margin:6px 4px 0}
.card .meta{margin:3px 4px 0}
.card .stars{margin:1px 4px 0}
.tabs{left:506px;top:533px;width:155px;height:200px;border:1px solid var(--line)}
.tabs .head{display:flex;height:26px;background:var(--green);font-size:8px;color:#fff}
.tabs .head span{flex:1;display:flex;align-items:center;justify-content:center}
.tabs .head span.on{background:var(--green-dark)}
.tab-item{display:flex;gap:5px;padding:5px 5px 0 5px;height:58px}
.tab-item .ph{width:47px;height:47px;flex:none}
.tab-item h5{font-weight:400;font-size:8px;line-height:12px}
.tab-item .meta{margin:3px 0 0;font-size:5.4px;line-height:9px}
.ad-side{left:506px;top:752px;width:155px;height:70px;background:linear-gradient(180deg,#f2f4f6,#dfe6ee)}
.ad-side .brand{position:absolute;left:4px;bottom:3px;font-size:8px;font-weight:600;color:#333}
.ad-side .more{position:absolute;right:5px;bottom:3px;background:#f3c244;color:#222;font-size:5.5px;padding:1px 5px;border-radius:2px}
.video{position:absolute;top:823px;height:88px}
.play{position:absolute;left:50%;top:50%;width:20px;height:12px;margin:-6px 0 0 -10px;background:var(--red);border-radius:3px}
.subscribe{left:506px;top:852px;width:155px}
.subscribe p{font-size:7.2px;color:var(--grey);margin-top:9px;letter-spacing:.2px}
.subscribe .form{display:flex;margin-top:7px;height:21px}
.subscribe .field{flex:1;border:1px solid var(--line);font-size:6.5px;color:#555;padding:6px 5px}
.subscribe .go{width:46px;background:var(--green);color:#fff;font-size:8px;display:flex;align-items:center;justify-content:center}
.ad-bottom{left:61px;top:951px;width:600px;height:51px;background:linear-gradient(90deg,var(--blue) 0%,var(--blue-deep) 30%,#4a9fe8 60%,var(--blue) 100%)}
.footer-rule{left:0;top:1042px;width:720px;border-top:1px solid var(--line)}
.foot-col{position:absolute;top:1070px}
.foot-col h6{font-weight:300;font-size:13px;color:#666;display:flex;align-items:center;gap:6px}
.foot-col ul{list-style:none;margin-top:8px;font-size:7.2px;line-height:13.7px;color:var(--grey)}
.foot-col p{margin-top:9px;font-size:7.2px;line-height:11px;color:var(--grey);width:195px}
.bottombar{left:0;top:1174px;width:720px;height:26px;background:var(--green);color:#e8f6ee;font-size:7.5px}
.bottombar .copy{position:absolute;left:61px;top:8px}
.bottombar .links{position:absolute;right:58px;top:0;display:flex;height:26px}
.bottombar .links span{display:flex;align-items:center;padding:0 6px;border-left:1px solid rgba(255,255,255,.3);font-size:6.5px}
</style>
</head>
<body>

<header>
  <div class="abs topbar">
    <span class="abs welcome">Welcome To Our site</span>
    <span class="abs social">kinlobby · murlotalk · pixagrove</span>
  </div>
  <div class="abs logo">The Bright Meadow.</div>
  <div class="abs ad-top">468x60 Banner Advertisement</div>
  <nav class="abs nav">
    <a class="active">ABOUT US</a><a>MOVE</a><a>GLOW</a><a>ESCAPE</a><a>BE</a><a>CONTACT US</a>
  </nav>
  <div class="abs search">Search</div>
  <div class="abs search-btn">
    <svg width="16" height="15" viewBox="0 0 16 15"><circle cx="7.5" cy="7" r="3" fill="none" stroke="#fff" stroke-width="1.3"/><line x1="9.7" y1="9.2" x2="11.5" y2="11" stroke="#fff" stroke-width="1.4"/></svg>
  </div>
</header>

<section class="abs hero">
  <div class="hero-photo" role="img" aria-label="Photo of women doing yoga on mats in a bright room"></div>
  <h1>Lorem ipsum dolor sit amet,<br>consectetur.</h1>
  <h2>Aliquam laoreet libero metus, et rhoncus</h2>
  <p>Lid est laborum dolo rumes fugats untras. Et harums ser quidem rerum facilis dolores nemis omnis fugiats vitaes nemo minima rerums unsers sadips amets.</p>
  <div class="btn">
    <svg width="12" height="12" viewBox="0 0 12 12"><circle cx="6" cy="6" r="6" fill="#1b7a3f"/><path d="M3.3 6.2l1.9 1.8 3.5-3.6" fill="none" stroke="#fff" stroke-width="1.3"/></svg>
    READ MORE
  </div>
  <div class="arrow" style="left:15px"><svg width="12" height="12" viewBox="0 0 12 12"><path d="M7 3L4 6l3 3" fill="none" stroke="#8cc9a2" stroke-width="1.2"/></svg></div>
  <div class="arrow" style="right:15px"><svg width="12" height="12" viewBox="0 0 12 12"><path d="M5 3l3 3-3 3" fill="none" stroke="#999" stroke-width="1.2"/></svg></div>
</section>

<section class="abs features">
  <div class="feature" style="left:-5px">
    <div class="icon" style="background:var(--green)"><svg width="18" height="18" viewBox="0 0 18 18"><circle cx="9" cy="10" r="6" fill="#fff"/><path d="M9 4c0-2 1-3 3-3" stroke="#fff" stroke-width="1.3" fill="none"/></svg></div>
    <h3>NUTRITION</h3>
    <p>Lorem ipsum dolor sit amet, consectetur adipiscing elit. Aliquam et odio id nibh placerat auctor.</p>
  </div>
  <div class="feature" style="left:152px">
    <div class="icon" style="background:#6a6a6a"><svg width="18" height="18" viewBox="0 0 18 18"><path d="M5 16L8 4h2l3 12" fill="none" stroke="#fff" stroke-width="1.8"/><circle cx="9" cy="3" r="1.6" fill="#fff"/></svg></div>
    <h3>FITNESS</h3>
    <p>Lorem ipsum dolor sit amet, consectetur adipiscing elit. Aliquam et odio id nibh placerat auctor.</p>
  </div>
  <div class="feature" style="left:308px">
    <div class="icon" style="background:#6a6a6a"><svg width="18" height="18" viewBox="0 0 18 18"><circle cx="9" cy="4" r="2" fill="#fff"/><path d="M3 14c2-1 3-1 6-1s4 0 6 1M9 7v5M5 10l4-2 4 2" fill="none" stroke="#fff" stroke-width="1.6"/></svg></div>
    <h3>YOGA</h3>
    <p>Lorem ipsum dolor sit amet, consectetur adipiscing elit. Aliquam et odio id nibh placerat auctor.</p>
  </div>
  <div class="feature" style="left:472px">
    <div class="icon" style="background:#6a6a6a"><svg width="18" height="18" viewBox="0 0 18 18"><path d="M6 2v14M4 2v5h4V2M12 16V2c2 1 3 3 3 6h-3" fill="none" stroke="#fff" stroke-width="1.5"/></svg></div>
    <h3>RECIPES</h3>
    <p>Lorem ipsum dolor sit amet, consectetur adipiscing elit. Aliquam et odio id nibh placerat auctor.</p>
  </div>
</section>

<section>
  <div class="abs sec-title" style="left:61px;top:533px"><span class="ring"><svg width="8" height="7" viewBox="0 0 8 7"><rect width="8" height="7" rx="1" fill="#333"/></svg></span>Newest Stories</div>
  <div class="abs pager" style="left:449px;top:533px"><span>‹</span><span>›</span></div>

  <article class="abs story-lead">
    <div class="ph" role="img" aria-label="Photo of a smiling woman in a kitchen"></div>
    <h4>Marlo Dunning Freed From Jail After Tax Evasion.</h4>
    <div class="meta">Posted on <b>7 April, 2013</b></div>
    <div class="stars"><i>★★</i>★★★</div>
    <p>Dreaming of an overseas move can be so exciting that it is often hard to focus on the dreary matter of money – but some smart decisions and simple planning could save you thousands eirmod tempor invidunt ut labore et dolore magna aliquyam erat... <em>Continue Reading</em></p>
  </article>

  <article class="card" style="left:266px;top:559px">
    <div class="ph" role="img" aria-label="Photo of a smiling woman outdoors" style="background:linear-gradient(135deg,#f2eccd,#e6d28a)"></div>
    <h4>How to budget for living abroad</h4>
    <div class="meta">Posted on <b>7 April, 2013</b></div>
    <div class="stars"><i>★★</i>★★★</div>
  </article>
  <article class="card" style="left:375px;top:559px">
    <div class="ph" role="img" aria-label="Photo of a runner on a park path" style="background:linear-gradient(180deg,#6c9a3c,#9cbe6a)"></div>
    <h4>How to budget for living abroad</h4>
    <div class="meta">Posted on <b>7 April, 2013</b></div>
    <div class="stars"><i>★★</i>★★★</div>
  </article>
  <article class="card" style="left:266px;top:662px">
    <div class="ph" role="img" aria-label="Photo of olive oil poured onto a spoon" style="background:linear-gradient(135deg,#7ea83a,#d8d060)"></div>
    <h4>How to budget for living abroad</h4>
    <div class="meta">Posted on <b>7 April, 2013</b> By</div>
    <div class="stars"><i>★★</i>★★★</div>
  </article>
  <article class="card" style="left:375px;top:662px">
    <div class="ph" role="img" aria-label="Photo of a woman stretching on grass" style="background:linear-gradient(180deg,#5d8fa8,#8ab64e)"></div>
    <h4>How to budget for living abroad</h4>
    <div class="meta">Posted on <b>7 April, 2013</b></div>
    <div class="stars"><i>★★</i>★★★</div>
  </article>
</section>

<aside>
  <div class="abs tabs">
    <div class="head"><span class="on">Popular</span><span>Recent</span><span>Comments</span></div>
    <div class="tab-item">
      <div class="ph" role="img" aria-label="Photo of a woman doing a beach stretch" style="background:linear-gradient(180deg,#d8e4ee,#c8b08c)"></div>
      <div><h5>How to budget for living abroad</h5><div class="meta">Posted on <b>7 April, 2013</b><br>By <b>Contantry popilar</b></div></div>
    </div>
    <div class="tab-item">
      <div class="ph" role="img" aria-label="Photo of a person jumping on a meadow" style="background:linear-gradient(180deg,#3c78b8,#7fb04a)"></div>
      <div><h5>How to budget for living abroad</h5><div class="meta">Posted on <b>7 April, 2013</b><br>By <b>Ipsum dolor</b></div></div>
    </div>
    <div class="tab-item">
      <div class="ph" role="img" aria-label="Photo of a family cycling" style="background:linear-gradient(180deg,#4a8ac8,#6f9a48)"></div>
      <div><h5>How to budget for living abroad</h5><div class="meta">Posted on <b>7 April, 2013</b><br>By <b>Lorem</b></div></div>
    </div>
  </div>

  <div class="abs ad-side" role="img" aria-label="E-reader advertisement with book covers">
    <span class="brand">pageleaf reader</span>
    <span class="more">Learn more</span>
  </div>

  <div class="abs subscribe">
    <div class="sec-title"><span class="ring"><svg width="8" height="6" viewBox="0 0 8 6"><rect x=".5" y=".5" width="7" height="5" fill="none" stroke="#333"/><path d="M.5.5L4 3.5 7.5.5" fill="none" stroke="#333"/></svg></span>Subscribe to newsletters</div>
    <p>Subscribe to our email newsletter.</p>
    <div class="form"><div class="field">Enter your email</div><div class="go">Subscribe</div></div>
  </div>
</aside>

<section>
  <div class="abs sec-title" style="left:61px;top:794px"><span class="ring"><svg width="7" height="7" viewBox="0 0 7 7"><path d="M1 0l6 3.5L1 7z" fill="#333"/></svg></span>Featured Video</div>
  <div class="abs pager" style="left:449px;top:794px"><span>‹</span><span>›</span></div>
  <div class="video" style="left:61px;width:132px;background:linear-gradient(135deg,#f7d9a0,#e59a4c)" role="img" aria-label="Video still of a couple running at sunset"><span class="play"></span></div>
  <div class="video" style="left:203px;width:134px;background:linear-gradient(180deg,#dfe9f0,#7cb34a)" role="img" aria-label="Video still of a parent playing with a child in a park"><span class="play"></span></div>
  <div class="video" style="left:346px;width:133px;background:linear-gradient(180deg,#c9b3d4,#e2a04c)" role="img" aria-label="Video still of a woman stretching on a road at dusk"><span class="play"></span></div>
</section>

<div class="abs ad-bottom" role="img" aria-label="Full-width advertisement banner"></div>

<footer>
  <div class="abs footer-rule"></div>
  <div class="foot-col" style="left:61px">
    <h6><svg width="16" height="16" viewBox="0 0 16 16"><circle cx="8" cy="8" r="7.3" fill="none" stroke="#666" stroke-width="1.2"/><rect x="7.3" y="6.5" width="1.4" height="5.5" fill="#666"/><circle cx="8" cy="4.4" r=".9" fill="#666"/></svg>About Company</h6>
    <p>Nullam ut commodo velit. Quisque sit amet arcu nisi. Sed id massa et mauris lacinia condimentum. In luctus suscipit laoreet. Suspendisse a arcu quis neque tincidunt posuere sagittis ac lacus. Aenean tristique accumsan ipsum vitae molestie. Etiam vulputate.</p>
  </div>
  <div class="foot-col" style="left:312px">
    <h6>Support</h6>
    <ul><li>Support home</li><li>Tablon Support</li><li>Knowledge base</li></ul>
  </div>
  <div class="foot-col" style="left:454px">
    <h6>Downloads</h6>
    <ul><li>Quillsoft Office</li><li>Panes 8</li><li>Talkwave</li><li>Tablon User Guide</li></ul>
  </div>
  <div class="foot-col" style="left:604px">
    <h6>Support</h6>
    <ul><li>Support home</li><li>Tablon Support</li><li>Knowledge base</li></ul>
  </div>
  <div class="abs bottombar">
    <span class="copy">© 2014 Yoursite - All rights reserved.</span>
    <div class="links"><span>kinlobby</span><span>murlotalk</span><span>pixagrove</span></div>
  </div>
</footer>

</body>
</html>
```